Website for Cedar Brook Fellowship Church

Wordpress website design required for Cedar Brook Fellowship Church. We are a family oriented church catering for age groups from school age to elderly people. The church has a wide variety of activities which it coordinates. The idea is to describe the activities on the activities page, but cross-link them to show which would be applicable to the different age groups.

We would like an inviting website which is easy to read and navigate.

Target Market(s)

Very wide audience - from school age youth to elderly people, so design and style should cater for both audiences.

Industry/Entity Type

Church

Coding

Coded - Design and coding required

Number of Pages Required

5+ page

Font styles to use
Sans Serif

Colors
0255a3
ffffff
0792cd
f78f20

Requirements
Must have
• Inviting website.
• Clear readable font.
• Space to import photos to balance text on each page.
• Need to project a dynamic and progressive feel for the church.
• Easy to navigate.
Nice to have
• Scrolling photos on pages. Ability to enter questions/ comments/prayer requests on Home page.
Should not have
• Conservative audience, so should not be too bold.

```html
<!DOCTYPE html>
<html lang="en">
<head>
<meta charset="UTF-8">
<title>Cedar Brook Fellowship Church</title>
<link href="https://fonts.googleapis.com/css2?family=Poppins:wght@300;400;500&family=Arimo:wght@400&display=swap" rel="stylesheet">
<style>
:root{
  --gold:#a08a50;
  --gold-dark:#8a7340;
  --button:#a99461;
  --navy:#1f3555;
  --ink:#222222;
  --grey-text:#8c8c8c;
  --grey-light:#9d9d9d;
  --band:#f0f0f0;
  --white:#ffffff;
  --rule:#9a9a9a;
}
*{margin:0;padding:0;box-sizing:border-box;}
html,body{width:1093px;height:1200px;overflow:hidden;background:var(--white);}
body{font-family:"Poppins",sans-serif;position:relative;}
.page{position:relative;width:1093px;height:1200px;overflow:hidden;}

.hero{position:absolute;left:0;top:0;width:1093px;height:432px;
  background:linear-gradient(180deg,#f3d4b0 0%,#e0a970 35%,#b8824a 70%,#8d6a46 100%);}
.hero-photo{position:absolute;inset:0;
  background:radial-gradient(ellipse at 60% 40%,rgba(255,236,205,.75) 0%,rgba(240,190,130,.3) 45%,rgba(120,85,50,0) 75%);}
.main-nav{position:absolute;left:0;top:0;width:1093px;height:54px;background:rgba(250,232,214,.6);
  border-bottom:1px solid rgba(255,255,255,.5);}
.main-nav a{position:absolute;top:20px;font-size:12.5px;letter-spacing:1.6px;color:var(--gold-dark);text-decoration:none;font-weight:400;}
.main-nav a.active{font-weight:500;}
.brand{position:absolute;left:0;width:1093px;top:177px;text-align:center;}
.brand-name{display:inline-flex;align-items:center;gap:10px;font-size:27px;font-weight:400;color:var(--navy);}
.brand-dot{width:18px;height:18px;border-radius:50%;background:var(--navy);}
.welcome{position:absolute;left:0;width:1093px;top:263px;text-align:center;font-family:"Arimo",sans-serif;
  font-size:12.6px;line-height:19.2px;color:var(--ink);}

.info-band{position:absolute;left:0;top:432px;width:1093px;height:114px;background:var(--white);}
.info-block{position:absolute;top:26px;}
.info-title{font-size:12.5px;color:var(--gold);font-weight:400;letter-spacing:.3px;margin-bottom:8px;}
.info-text{font-size:10.5px;line-height:19px;color:#555;text-transform:uppercase;letter-spacing:.2px;}
.info-icon{position:absolute;top:24px;}
.info-divider{position:absolute;left:546px;top:10px;width:1px;height:93px;background:var(--rule);}

.about{position:absolute;left:0;top:546px;width:1093px;height:295px;background:var(--band);}
.section-title{font-size:20px;font-weight:400;color:var(--gold);letter-spacing:.3px;}
.about .section-title{position:absolute;left:78px;top:27px;}
.about-lead{position:absolute;left:78px;top:72px;width:540px;font-size:15px;line-height:19.5px;color:var(--grey-text);font-weight:300;}
.about-body{position:absolute;left:78px;top:128px;width:540px;font-size:11.5px;line-height:19.2px;color:var(--grey-light);font-weight:300;}
.btn-more{position:absolute;left:78px;top:220px;width:136px;height:38px;background:var(--button);color:var(--white);
  font-size:11.5px;display:flex;align-items:center;justify-content:center;letter-spacing:.3px;}
.photo{position:absolute;}
.photo-prayer{left:645px;top:52px;width:203px;height:117px;background:linear-gradient(120deg,#f1e2c4 0%,#b99566 45%,#4a3522 100%);}
.photo-cross{left:798px;top:132px;width:217px;height:130px;border-left:2px solid var(--white);border-top:2px solid var(--white);
  background:linear-gradient(180deg,#d7a15d 0%,#b5652a 45%,#5c2f12 75%,#140a04 100%);}

.activities-head{position:absolute;left:0;top:841px;width:1093px;height:109px;text-align:center;}
.activities-head .section-title{position:absolute;left:0;width:1093px;top:26px;}
.activities-sub{position:absolute;left:0;width:1093px;top:67px;font-size:13.3px;color:#666;font-weight:300;}

.activity-grid{position:absolute;left:0;top:950px;width:1093px;height:250px;display:grid;
  grid-template-columns:repeat(4,1fr);grid-template-rows:158px 92px;}
.tile{position:relative;overflow:hidden;}
.tile-1{background:linear-gradient(160deg,#bdb397 0%,#6b6656 50%,#3c3b38 100%);}
.tile-2{background:linear-gradient(160deg,#d3b89a 0%,#7a5a42 45%,#3a2a20 100%);}
.tile-3{background:linear-gradient(135deg,#2f55b5 0%,#c73a3a 35%,#2e8a3e 65%,#d8b13a 100%);}
.tile-4{background:linear-gradient(160deg,#d9c3a6 0%,#9b7a5c 50%,#5b4335 100%);}
.tile-5{background:linear-gradient(180deg,#e4a250 0%,#b86a2c 60%,#5e3416 100%);}
.tile-6{background:linear-gradient(180deg,#9aa7b6 0%,#c7ccd2 50%,#8a8d90 100%);}
.tile-7{background:linear-gradient(180deg,#f3eee6 0%,#ddd3c4 60%,#a58c6a 100%);}
.tile-8{background:linear-gradient(160deg,#1d3a44 0%,#6c8f95 50%,#163037 100%);}
.tile-overlay{position:absolute;inset:0;background:rgba(40,40,40,.45);color:var(--white);text-align:center;}
.tile-plus{position:absolute;left:0;width:100%;top:40px;height:26px;}
.tile-caption{position:absolute;left:14px;right:14px;top:88px;font-size:12.8px;line-height:24px;font-weight:300;}
</style>
</head>
<body>
<div class="page">

  <header class="hero">
    <div class="hero-photo" role="img" aria-label="Cross silhouetted against a glowing sunset sky"></div>
    <nav class="main-nav">
      <a class="active" style="left:103px">HOME</a>
      <a style="left:225px">AGE GROUP</a>
      <a style="left:384px">ACTIVITES</a>
      <a style="left:537px">EVENTS CALENDAR</a>
      <a style="left:747px">ABOUT CBFC</a>
      <a style="left:918px">CONTACT</a>
    </nav>
    <div class="brand">
      <span class="brand-name"><span class="brand-dot"></span>Cedar Brook Fellowship Church</span>
    </div>
    <p class="welcome">
      welcome text here, welcome text here, welcome text here, welcome text here, welcome text here,<br>
      welcome text here, welcome text here, welcome text here, welcome text here, welcome text here,<br>
      welcome text here, welcome text here, welcome text here, welcome text here, welcome text here,<br>
      welcome text here,
    </p>
  </header>

  <section class="info-band">
    <svg class="info-icon" style="left:84px" width="46" height="46" viewBox="0 0 46 46" fill="none" stroke="#a08a50" stroke-width="1.6">
      <rect x="2" y="6" width="42" height="38" rx="2"/>
      <line x1="2" y1="14" x2="44" y2="14"/>
      <line x1="12" y1="2" x2="12" y2="9"/><line x1="34" y1="2" x2="34" y2="9"/>
      <rect x="9" y="20" width="5" height="4"/><rect x="18" y="20" width="5" height="4"/><rect x="27" y="20" width="5" height="4"/><rect x="36" y="20" width="4" height="4"/>
      <rect x="9" y="28" width="5" height="4"/><rect x="18" y="28" width="5" height="4"/><rect x="27" y="28" width="5" height="4"/><rect x="36" y="28" width="4" height="4"/>
      <rect x="9" y="36" width="5" height="4"/><rect x="18" y="36" width="5" height="4"/><rect x="27" y="36" width="5" height="4"/>
    </svg>
    <div class="info-block" style="left:146px">
      <h3 class="info-title">MINISTER'S WEEKLY MESSAGE</h3>
      <p class="info-text">"Lorem Ipsum is simply dummy text of the printing and typeset-<br>ting industry.</p>
    </div>
    <div class="info-divider"></div>
    <svg class="info-icon" style="left:566px" width="42" height="44" viewBox="0 0 42 44" fill="none" stroke="#a08a50" stroke-width="1.8" stroke-linecap="round">
      <circle cx="21" cy="24" r="16"/>
      <path d="M3 9 A7 7 0 0 1 12 3"/><path d="M30 3 A7 7 0 0 1 39 9"/>
      <line x1="21" y1="14" x2="21" y2="25"/><line x1="21" y1="25" x2="14" y2="25"/>
      <line x1="10" y1="38" x2="7" y2="42"/><line x1="32" y1="38" x2="35" y2="42"/>
    </svg>
    <div class="info-block" style="left:626px">
      <h3 class="info-title">SERVICE TIME</h3>
      <p class="info-text">8:30 AM - Bible Study 10AM-Awaken Service &amp; Bible Study<br>8:30 AM - Bible Study 10AM-Awaken Service &amp; Bible Study</p>
    </div>
  </section>

  <section class="about">
    <h2 class="section-title">ABOUT CBFC</h2>
    <p class="about-lead">Lorem Ipsum is simply dummy text of the printing and typesetting indus-try. Lorem Ipsum has been the industry's</p>
    <p class="about-body">Lorem Ipsum is simply dummy text of the printing and typesetting industry. Lorem Ipsum has been the industry's standard dummy text ever since the 1500s, when an unknown printer took a galley of type and scrambled it to make a type specimen book. It has survived not only five centuries, but also the leap into electronic typesetting, remaining essentially unchanged. It was</p>
    <a class="btn-more">KNOW MORE</a>
    <div class="photo photo-prayer" role="img" aria-label="Hands folded in prayer over an open Bible"></div>
    <div class="photo photo-cross" role="img" aria-label="Person kneeling beside a cross on a hill at sunset"></div>
  </section>

  <section class="activities-head">
    <h2 class="section-title">CHURCH ACTIVITIES</h2>
    <p class="activities-sub">Lorem Ipsum is simply dummy text of the printing and typesetting industry.</p>
  </section>

  <section class="activity-grid">
    <div class="tile tile-1" role="img" aria-label="Figure with arms raised on a hilltop">
      <div class="tile-overlay">
        <svg class="tile-plus" viewBox="0 0 273 26"><line x1="136.5" y1="1" x2="136.5" y2="25" stroke="#fff" stroke-width="3"/><line x1="125" y1="13" x2="148" y2="13" stroke="#fff" stroke-width="3"/></svg>
        <p class="tile-caption">Lorem Ipsum is simply dummy text of the printing and typesetting industry.</p>
      </div>
    </div>
    <div class="tile tile-2" role="img" aria-label="Congregation seated in church pews"></div>
    <div class="tile tile-3" role="img" aria-label="Colourful stained glass window"></div>
    <div class="tile tile-4" role="img" aria-label="Group reading hymn books together"></div>
    <div class="tile tile-5" role="img" aria-label="Cross against an orange sunset"></div>
    <div class="tile tile-6" role="img" aria-label="Church bell tower under a cloudy sky"></div>
    <div class="tile tile-7" role="img" aria-label="Bright church interior with altar"></div>
    <div class="tile tile-8" role="img" aria-label="Young people worshipping"></div>
  </section>

</div>
</body>
</html>
```